Maputo Tessel Renewal Scheme (TRZ) Project Needs a Web Design

We need a web design for a new project. The Hollin Trust and the Velder Civic Council has awarded Brelvik a contract valued at US $1.1 million to provide consulting services for the design of the Tessel Renewal Scheme (TRS) of the "Baixa", or central business district, of the historic capital of Mozambique - Maputo. The primary goal of the project website is to foster public engagement: generate public awareness and interest in the project, solicit public input and feedback, and encourage involvement and action related to the project.
We would like to see designs that mirror the colors of the city of Maputo flag (light green and dark green with yellow accents). The final design should be interactive and should communicate urban planning, development, and civic engagement.
We would like to use a simple, open source platform that will allow us to easily make text and image updates. We will not have an in-house web developer helping to manage the site, thus we need an easy way to access the content management system "back-end" or make simple updates.
Target Market(s)
Primary audience: citizens of Maputo. Secondary audiences: project staff, contractor staff, client staff, wider development community.
Industry/Entity Type
Business
Requirements
Must have
- The website should have the following pages:
Homepage (landing page)
About (Vision/why)
Data
Events (public engagements)
Blog
Contact Us
Stakeholder Portal
Nice to have
- The Homepage could use flash to slide through 3-4 photos automatically. The homepage would ideally have a top bar or side bar linking to the other webpages, with a road map at the bottom.
Space to put photos and text on each webpage.
The Events page could have a calendar to show when specific events are taking place.

```html
<!DOCTYPE html>
<html lang="en">
<head>
<meta charset="utf-8">
<title>Tessel Renewal Scheme – Home</title>
<link rel="stylesheet" href="https://fonts.googleapis.com/css2?family=Bebas+Neue&family=Arimo:wght@400;700&family=Gelasio:wght@500&display=swap">
<style>
:root{
  --lime:#c9f65c;
  --leaf:#5c9a12;
  --nav:#6fa81c;
  --nav-edge:#a9d84a;
  --active:#00a000;
  --accent:#ffff00;
  --charcoal:#404040;
  --footer:#333333;
  --paper:#eeeeee;
  --white:#ffffff;
  --rule:#cccccc;
  --body-text:#7a7a7a;
  --ink:#111111;
  --muted:#7d7d7d;
}
*{margin:0;padding:0;box-sizing:border-box}
html,body{width:1155px;height:1200px;overflow:hidden}
body{position:relative;background:var(--paper);font-family:Arimo,Arial,sans-serif}
.abs{position:absolute}

.site-header{left:0;top:0;width:1155px;height:97px;background:linear-gradient(var(--lime),#a6dc3a 55%,var(--leaf))}
.brand{left:184px;top:30px;width:100px;display:flex;align-items:center;gap:6px;font-weight:700;font-size:12px;line-height:14px;color:var(--footer)}
.brand-dot{width:14px;height:14px;border-radius:50%;background:var(--active);flex:none}
.badge{left:288px;top:21px;width:101px;height:65px;background:var(--active);box-shadow:2px 3px 4px rgba(0,0,0,.3)}
.badge span{position:absolute;left:16px;top:10px;width:69px;height:43px;border:1px solid var(--accent);background:#11c011}
.main-nav{left:403px;top:35px;display:flex;gap:3px}
.main-nav a{display:block;width:92px;height:37px;line-height:35px;text-align:center;font-size:9.5px;color:var(--accent);text-decoration:none;background:var(--nav);border:1px solid var(--nav-edge)}
.main-nav a.current{background:var(--active);border-color:var(--white)}

.hero-band{left:0;top:97px;width:1155px;height:315px;background:var(--charcoal)}
.hero-frame{left:191px;top:11px;width:775px;height:293px;background:var(--white)}
.hero-slide{left:7px;top:6px;width:760px;height:281px;background:linear-gradient(#35589c,#6c8cc6 55%,#d9d3c4 78%,#4c5a34)}
.hero-caption{left:2px;top:246px;font-size:11px;font-family:Gelasio,Georgia,serif;color:#9a9a9a}

.content{left:184px;top:421px;width:788px;height:580px;background:var(--white);border:1px solid var(--rule)}
.card{top:9px;width:253px;height:344px;border:1px solid var(--rule);border-radius:7px}
.card h2{position:absolute;left:8px;top:2px;font-family:"Bebas Neue",sans-serif;font-weight:400;font-size:31px;color:var(--ink)}
.card-photo{position:absolute;left:4px;top:40px;width:243px;height:122px}
.card p{position:absolute;left:7px;top:180px;width:240px;font-size:12px;line-height:13.7px;color:var(--body-text);text-align:justify}
.more{right:10px;top:370px;font-size:11px;color:var(--ink)}
.news-title{left:14px;top:389px;font-family:"Bebas Neue",sans-serif;font-weight:400;font-size:32px;color:var(--ink)}
.news p{position:absolute;left:14px;width:757px;font-size:12px;line-height:13.7px;color:var(--body-text);text-align:justify}

.site-footer{left:0;top:1018px;width:1155px;height:121px;background:var(--footer)}
.footer-nav{left:206px;top:15px;list-style:none;font-family:Gelasio,Georgia,serif;font-size:12px;line-height:16.4px;color:var(--white)}
.footer-mark{left:510px;top:44px;width:135px;display:flex;align-items:center;gap:6px;font-weight:700;font-size:11px;color:#4a4a4a}
.footer-mark i{width:12px;height:12px;border-radius:50%;background:#4a4a4a;flex:none}
.social{left:830px;top:14px;width:135px;display:flex;justify-content:center;gap:10px;font-size:10px;color:#aab4cc}
.social span{display:flex;align-items:center;gap:4px}
.social i{width:10px;height:10px;background:#3e5f99}
.social span+span i{background:#48a6d0}
.contact-label{left:830px;top:44px;width:135px;text-align:center;font-family:"Bebas Neue",sans-serif;font-size:28px;color:var(--muted)}
.contact-phone{left:830px;top:77px;width:135px;text-align:center;font-family:"Bebas Neue",sans-serif;font-size:31px;color:var(--muted)}

.copyright-bar{left:0;top:1139px;width:1155px;height:61px;background:linear-gradient(var(--lime),#a3d93a 50%,var(--leaf));text-align:center;font-size:12px;color:var(--white);padding-top:23px}
</style>
</head>
<body>

<header class="site-header abs">
  <div class="brand abs"><span class="brand-dot"></span>Velder Civic Council</div>
  <div class="badge abs"><span></span></div>
  <nav class="main-nav abs">
    <a class="current" href="#">Home</a>
    <a href="#">Data</a>
    <a href="#">Events</a>
    <a href="#">Blog</a>
    <a href="#">Contact</a>
    <a href="#">Stakeholder Portal</a>
  </nav>
</header>

<section class="hero-band abs">
  <div class="hero-frame abs">
    <div class="hero-slide abs" role="img" aria-label="City skyline with a white cathedral tower and a tall hotel under a blue sky">
      <span class="hero-caption abs">Lorem ipsum dolor sit amet</span>
    </div>
  </div>
</section>

<main class="content abs">
  <article class="card abs" style="left:6px">
    <h2>Top 1</h2>
    <div class="card-photo" role="img" aria-label="Cream civic building with domes and palm trees" style="background:linear-gradient(#6fa0d8,#e8dcb8 55%,#5f7a3c)"></div>
    <p>Lorem ipsum dolor sit amet, consectetur adipisicing elit, sed do eiusmod tempor incididunt ut labore et dolore magna aliqua. Ut enim ad minim veniam, quis nostrud exercitation ullamco laboris nisi ut aliquip ex ea commodo consequat. Duis aute irure dolor in reprehenderit in voluptate velit esse cillum dolore eu fugiat nulla pariatur. Excepteur sint occaecat cupidatat non proident, sunt in culpa qui officia deserunt mollit anim id est laborum.</p>
  </article>
  <article class="card abs" style="left:269px">
    <h2>Top 2</h2>
    <div class="card-photo" role="img" aria-label="Aerial view of a city roundabout and surrounding blocks" style="background:linear-gradient(#8a8e80,#6f7f5a 50%,#a9a08a)"></div>
    <p>Lorem ipsum dolor sit amet, consectetur adipisicing elit, sed do eiusmod tempor incididunt ut labore et dolore magna aliqua. Ut enim ad minim veniam, quis nostrud exercitation ullamco laboris nisi ut aliquip ex ea commodo consequat. Duis aute irure dolor in reprehenderit in voluptate velit esse cillum dolore eu fugiat nulla pariatur. Excepteur sint occaecat cupidatat non proident, sunt in culpa qui officia deserunt mollit anim id est laborum.</p>
  </article>
  <article class="card abs" style="left:530px">
    <h2>Top 3</h2>
    <div class="card-photo" role="img" aria-label="Historic railway station facade with a domed clock tower" style="background:linear-gradient(90deg,#3c5a30,#d8d2bc 45%,#9bb6d8)"></div>
    <p style="top:177px">Lorem ipsum dolor sit amet, consectetur adipisicing elit, sed do eiusmod tempor incididunt ut labore et dolore magna aliqua. Ut enim ad minim veniam, quis nostrud exercitation ullamco laboris nisi ut aliquip ex ea commodo consequat. Duis aute irure dolor in reprehenderit in voluptate velit esse cillum dolore eu fugiat nulla pariatur. Excepteur sint occaecat cupidatat non proident, sunt in culpa qui officia deserunt mollit anim id est laborum.</p>
  </article>

  <a class="more abs">more &gt;&gt;</a>

  <section class="news">
    <h2 class="news-title abs">News</h2>
    <p style="top:420px">Lorem ipsum dolor sit amet, consectetur adipisicing elit, sed do eiusmod tempor incididunt ut labore et dolore magna aliqua. Ut enim ad minim veniam, quis nostrud exercitation ullamco laboris nisi ut aliquip ex ea commodo consequat. Duis aute irure dolor in reprehenderit in voluptate velit esse cillum dolore eu fugiat nulla pariatur. Excepteur sint occaecat cupidatat non proident, sunt in culpa qui officia deserunt mollit anim id est laborum.</p>
    <p style="top:509px">Lorem ipsum dolor sit amet, consectetur adipisicing elit, sed do eiusmod tempor incididunt ut labore et dolore magna aliqua. Ut enim ad minim veniam, quis nostrud exercitation ullamco laboris nisi ut aliquip ex ea commodo consequat. Duis aute irure dolor in reprehenderit in voluptate velit esse cillum dolore eu fugiat nulla pariatur. Excepteur sint occaecat cupidatat non proident, sunt in culpa qui officia deserunt mollit anim id est laborum.</p>
  </section>
</main>

<footer class="site-footer abs">
  <ul class="footer-nav abs">
    <li>Home</li><li>Data</li><li>Events</li><li>Blog</li><li>Contact</li><li>Stakeholder Portal</li>
  </ul>
  <div class="footer-mark abs"><i></i>Velder Civic Council</div>
  <div class="social abs"><span><i></i>Friendwall</span><span><i></i>Chirplet</span></div>
  <div class="contact-label abs">Contact Us</div>
  <div class="contact-phone abs">55012-30418</div>
</footer>

<div class="copyright-bar abs">Copyright &copy; 2013. All Rights Reserved.</div>

</body>
</html>
```